Design for an iOS and Android app managing shopping list

The app allows you to keep manage shopping lists, each shopping list being made of items to buy...
We need a design for the 3 screens of the app:
a) global view showing list of (shopping) list
b) form enabling to edit the name of a (shopping) list
c) detailed view listing the contents/items of a (shopping) list
d) 1 text page [not illustrated]
2 "alerts" items are also to be designed: confirm and error pop ups.
No specific guidelines, nor logo or whatever.
It will be a free app distributed on iOS and Androïd.
We just want to make it looking nice & very usable for end users.

```html
<!DOCTYPE html>
<html lang="en">
<head>
<meta charset="utf-8">
<title>Shopping List App – Screens</title>
<link href="https://fonts.googleapis.com/css2?family=Roboto:wght@300;400;500&display=swap" rel="stylesheet">
<style>
  :root {
    --navy: #35355a;
    --navy-dim: rgba(53, 53, 90, 0.9);
    --green: #5bb58a;
    --paper: #f7f7f7;
    --field: #efefef;
    --line: #e4e4e4;
    --text: #6e6e6e;
    --placeholder: #c4c4c4;
    --arrow: #cfcfcf;
    --red: #e5484d;
    --white: #ffffff;
    --stage: #ffffff;
  }
  * { box-sizing: border-box; margin: 0; padding: 0; }
  html, body { width: 1200px; height: 600px; overflow: hidden; background: var(--stage); }
  body { font-family: "Roboto", Arial, sans-serif; }

  .canvas { position: relative; width: 1200px; height: 600px; overflow: hidden; background: var(--stage); }

  .screen {
    position: absolute; top: 149px; width: 176px; height: 310px;
    background: var(--paper); overflow: hidden;
    box-shadow: 0 2px 10px rgba(0, 0, 0, 0.12);
  }
  .screen--lists { left: 59px; }
  .screen--items { left: 286px; background: var(--navy); }
  .screen--rename { left: 513px; background: var(--white); }
  .screen--confirm { left: 740px; }
  .screen--error { left: 966px; background: var(--white); }

  .app-bar {
    height: 35px; background: var(--navy); color: var(--white);
    display: flex; align-items: center; justify-content: center; position: relative;
  }
  .app-bar__title {
    font-size: 8.8px; font-weight: 500; letter-spacing: 0.2px; line-height: 1;
    white-space: nowrap;
  }
  .app-bar__title span { font-weight: 300; }
  .app-bar__icon { position: absolute; left: 7px; top: 10px; width: 15px; height: 15px; }

  .entry {
    height: 28px; background: var(--field); display: flex; align-items: center;
    padding: 0 8px 0 15px; position: relative; font-size: 7.6px; color: var(--placeholder); font-weight: 300;
    border-bottom: 1px solid var(--line);
  }
  .entry::before { content: ""; width: 1px; height: 11px; background: var(--green); margin-right: 4px; }
  .entry--filled { color: var(--text); font-weight: 400; }
  .entry__add { position: absolute; right: 8px; top: 6px; width: 16px; height: 16px; }

  .list-row {
    height: 21.5px; display: flex; align-items: center; padding: 0 10px 0 11px;
    border-bottom: 1px solid var(--line); font-size: 7.8px; color: var(--text); font-weight: 300;
  }
  .list-row__arrow { width: 12px; height: 7px; margin-right: 9px; }
  .list-row__name { flex: 1; }
  .icon-x { width: 8px; height: 8px; }

  .bottom-bar {
    position: absolute; left: 0; right: 0; bottom: 0; height: 24px; background: var(--green);
    color: var(--white); font-size: 8.4px; font-weight: 500; display: flex; align-items: center; justify-content: center;
  }

  .section--pending { background: var(--green); padding-bottom: 5px; }
  .section--done { padding-top: 2px; }
  .section__label { height: 20px; display: flex; align-items: center; padding-left: 14px; color: var(--white); font-size: 10px; font-weight: 300; }
  .item-row { height: 21px; display: flex; align-items: center; padding: 0 12px 0 25px; color: var(--white); font-size: 7.6px; font-weight: 300; }
  .item-row__check { width: 8px; height: 8px; margin-right: 8px; }
  .item-row__name { flex: 1; }
  .item-row--done .item-row__name, .item-row--done .item-row__check { opacity: 0.3; }

  .save-button {
    height: 28px; background: var(--green); color: var(--white); font-size: 8.4px; font-weight: 500;
    display: flex; align-items: center; justify-content: center;
  }

  .scrim { position: absolute; inset: 0; background: var(--navy-dim); }

  .dialog { position: absolute; left: 18px; top: 89px; width: 136px; background: var(--white); box-shadow: 0 2px 6px rgba(0,0,0,0.25); }
  .screen--error .dialog { left: 19px; }
  .dialog__title { height: 21px; background: var(--navy); color: var(--white); font-size: 7.6px; font-weight: 400; display: flex; align-items: center; padding-left: 9px; }
  .dialog__body { padding: 13px 9px 0; color: var(--text); font-size: 9.6px; font-weight: 300; line-height: 12px; min-height: 52px; }
  .dialog__actions { display: flex; justify-content: space-between; padding: 6px 10px 9px; font-size: 6.6px; font-weight: 500; }
  .dialog__actions--single { justify-content: flex-end; }
  .dialog__action--cancel { color: #333; }
  .dialog__action--delete { color: var(--red); }
  .dialog__action--ok { color: #333; }

  .defs { position: absolute; width: 0; height: 0; }
</style>
</head>
<body>
<svg class="defs" aria-hidden="true">
  <defs>
    <symbol id="icon-close-circle" viewBox="0 0 16 16"><circle cx="8" cy="8" r="7.2" fill="none" stroke="#fff" stroke-width="1"/><path d="M5.5 5.5l5 5M10.5 5.5l-5 5" stroke="#fff" stroke-width="1"/></symbol>
    <symbol id="icon-back-circle" viewBox="0 0 16 16"><circle cx="8" cy="8" r="7.2" fill="none" stroke="#fff" stroke-width="1"/><path d="M11 8H5.2M7.6 5.5L5.1 8l2.5 2.5" fill="none" stroke="#fff" stroke-width="1"/></symbol>
    <symbol id="icon-add" viewBox="0 0 16 16"><circle cx="8" cy="8" r="7.2" fill="none" stroke="#5bb58a" stroke-width="1.1"/><path d="M8 4.2v7.6M4.2 8h7.6" stroke="#5bb58a" stroke-width="1.1"/></symbol>
    <symbol id="icon-arrow" viewBox="0 0 12 7"><path d="M0 3.5h11M8 0.6l3 2.9-3 2.9" fill="none" stroke="#cfcfcf" stroke-width="0.8"/></symbol>
    <symbol id="icon-x-red" viewBox="0 0 8 8"><path d="M0.5 0.5l7 7M7.5 0.5l-7 7" stroke="#e5484d" stroke-width="1"/></symbol>
    <symbol id="icon-x-white" viewBox="0 0 8 8"><path d="M0.5 0.5l7 7M7.5 0.5l-7 7" stroke="#fff" stroke-width="1"/></symbol>
    <symbol id="icon-box" viewBox="0 0 8 8"><rect x="0.5" y="0.5" width="7" height="7" fill="none" stroke="#fff" stroke-width="0.8"/></symbol>
    <symbol id="icon-box-checked" viewBox="0 0 8 8"><rect x="0.5" y="0.5" width="7" height="7" fill="none" stroke="#fff" stroke-width="0.8"/><path d="M2 4.2l1.5 1.5L6.2 2.6" fill="none" stroke="#fff" stroke-width="0.9"/></symbol>
  </defs>
</svg>

<main class="canvas">

  <!-- Lists overview -->
  <section class="screen screen--lists">
    <header class="app-bar"><svg class="app-bar__icon"><use href="#icon-close-circle"/></svg><h1 class="app-bar__title">YOUR LISTS</h1></header>
    <div class="entry">Add new shopping list<svg class="entry__add"><use href="#icon-add"/></svg></div>
    <div class="list-row"><svg class="list-row__arrow"><use href="#icon-arrow"/></svg><span class="list-row__name">Diner de ce soir</span><svg class="icon-x"><use href="#icon-x-red"/></svg></div>
    <div class="list-row"><svg class="list-row__arrow"><use href="#icon-arrow"/></svg><span class="list-row__name">Course Noel</span><svg class="icon-x"><use href="#icon-x-red"/></svg></div>
    <div class="list-row"><svg class="list-row__arrow"><use href="#icon-arrow"/></svg><span class="list-row__name">Courses NORDA</span><svg class="icon-x"><use href="#icon-x-red"/></svg></div>
    <div class="list-row"><svg class="list-row__arrow"><use href="#icon-arrow"/></svg><span class="list-row__name">Halvora</span><svg class="icon-x"><use href="#icon-x-red"/></svg></div>
    <div class="list-row"><svg class="list-row__arrow"><use href="#icon-arrow"/></svg><span class="list-row__name">Menage</span><svg class="icon-x"><use href="#icon-x-red"/></svg></div>
    <div class="list-row"><svg class="list-row__arrow"><use href="#icon-arrow"/></svg><span class="list-row__name">Cadeaux de noel</span><svg class="icon-x"><use href="#icon-x-red"/></svg></div>
    <div class="list-row"><svg class="list-row__arrow"><use href="#icon-arrow"/></svg><span class="list-row__name">Shopping list name</span><svg class="icon-x"><use href="#icon-x-red"/></svg></div>
    <footer class="bottom-bar">ABOUT US</footer>
  </section>

  <!-- List detail -->
  <section class="screen screen--items">
    <header class="app-bar"><svg class="app-bar__icon"><use href="#icon-back-circle"/></svg><h1 class="app-bar__title">LIST : <span>COURSE NORDA</span></h1></header>
    <div class="entry">Add new item<svg class="entry__add"><use href="#icon-add"/></svg></div>
    <div class="section section--pending">
      <div class="section__label">Pending</div>
      <div class="item-row"><svg class="item-row__check"><use href="#icon-box"/></svg><span class="item-row__name">Diner de ce soir</span><svg class="icon-x"><use href="#icon-x-white"/></svg></div>
      <div class="item-row"><svg class="item-row__check"><use href="#icon-box"/></svg><span class="item-row__name">Course Noel</span><svg class="icon-x"><use href="#icon-x-white"/></svg></div>
      <div class="item-row"><svg class="item-row__check"><use href="#icon-box"/></svg><span class="item-row__name">Courses NORDA</span><svg class="icon-x"><use href="#icon-x-white"/></svg></div>
      <div class="item-row"><svg class="item-row__check"><use href="#icon-box"/></svg><span class="item-row__name">Halvora</span><svg class="icon-x"><use href="#icon-x-white"/></svg></div>
      <div class="item-row"><svg class="item-row__check"><use href="#icon-box"/></svg><span class="item-row__name">Menage</span><svg class="icon-x"><use href="#icon-x-white"/></svg></div>
    </div>
    <div class="section section--done">
      <div class="section__label">Done</div>
      <div class="item-row item-row--done"><svg class="item-row__check"><use href="#icon-box-checked"/></svg><span class="item-row__name">Cadeaux de noel</span><svg class="icon-x"><use href="#icon-x-white"/></svg></div>
      <div class="item-row item-row--done"><svg class="item-row__check"><use href="#icon-box-checked"/></svg><span class="item-row__name">Shopping list name</span><svg class="icon-x"><use href="#icon-x-white"/></svg></div>
      <div class="item-row item-row--done"><svg class="item-row__check"><use href="#icon-box-checked"/></svg><span class="item-row__name">Shopping list name</span><svg class="icon-x"><use href="#icon-x-white"/></svg></div>
    </div>
  </section>

  <!-- Rename form -->
  <section class="screen screen--rename">
    <header class="app-bar"><svg class="app-bar__icon"><use href="#icon-back-circle"/></svg><h1 class="app-bar__title">UPADATE LIST NAME</h1></header>
    <div class="entry entry--filled">Diner de ce soir</div>
    <div class="save-button">SAVE</div>
  </section>

  <!-- Confirm delete -->
  <section class="screen screen--confirm">
    <header class="app-bar"><svg class="app-bar__icon"><use href="#icon-close-circle"/></svg><h1 class="app-bar__title">YOUR LISTS</h1></header>
    <div class="entry">Add new shopping list<svg class="entry__add"><use href="#icon-add"/></svg></div>
    <div class="list-row"><svg class="list-row__arrow"><use href="#icon-arrow"/></svg><span class="list-row__name">Diner de ce soir</span><svg class="icon-x"><use href="#icon-x-red"/></svg></div>
    <div class="list-row"><svg class="list-row__arrow"><use href="#icon-arrow"/></svg><span class="list-row__name">Course Noel</span><svg class="icon-x"><use href="#icon-x-red"/></svg></div>
    <div class="list-row"><svg class="list-row__arrow"><use href="#icon-arrow"/></svg><span class="list-row__name">Courses NORDA</span><svg class="icon-x"><use href="#icon-x-red"/></svg></div>
    <div class="list-row"><svg class="list-row__arrow"><use href="#icon-arrow"/></svg><span class="list-row__name">Halvora</span><svg class="icon-x"><use href="#icon-x-red"/></svg></div>
    <div class="list-row"><svg class="list-row__arrow"><use href="#icon-arrow"/></svg><span class="list-row__name">Menage</span><svg class="icon-x"><use href="#icon-x-red"/></svg></div>
    <div class="list-row"><svg class="list-row__arrow"><use href="#icon-arrow"/></svg><span class="list-row__name">Cadeaux de noel</span><svg class="icon-x"><use href="#icon-x-red"/></svg></div>
    <div class="list-row"><svg class="list-row__arrow"><use href="#icon-arrow"/></svg><span class="list-row__name">Shopping list name</span><svg class="icon-x"><use href="#icon-x-red"/></svg></div>
    <footer class="bottom-bar">ABOUT US</footer>
    <div class="scrim"></div>
    <div class="dialog" role="dialog">
      <div class="dialog__title">Remove the shopping list</div>
      <p class="dialog__body">Would you like to delete the shopping list?</p>
      <div class="dialog__actions"><span class="dialog__action--cancel">CANCEL</span><span class="dialog__action--delete">DELETE</span></div>
    </div>
  </section>

  <!-- Validation error -->
  <section class="screen screen--error">
    <header class="app-bar"><svg class="app-bar__icon"><use href="#icon-back-circle"/></svg><h1 class="app-bar__title">UPADATE LIST NAME</h1></header>
    <div class="entry entry--filled">Diner de ce soir</div>
    <div class="save-button">SAVE</div>
    <div class="scrim"></div>
    <div class="dialog" role="alertdialog">
      <div class="dialog__title">Warning</div>
      <p class="dialog__body">List name should have at least 1 character to be valid!</p>
      <div class="dialog__actions dialog__actions--single"><span class="dialog__action--ok">OK</span></div>
    </div>
  </section>

</main>
</body>
</html>
```